Golden Years Wellness Roadmap: This is my second book. The first was Eldercare Compass

I need a book cover design for: GOLDEN YEARS WELLNESS ROADMAP: A NO-EXPENSE METHOD FOR FINISHING YOUR LATER-LIFE MOSAIC WITH POOLED KVB CARE SCHEMES by Derek Holloway Neil Osgrove & Martin Quarles. This book is designed for business owners, CEO's, CFO's and Human Resources. The cover needs to be professional and focused on business. The purpose of this book is to educate business owners and their management about a zero cost retiree health plan. This is a first of it's kind solution that every business needs to learn about.

Target Market(s)

Business owners, CEO's, CFO's and Human Resources

Requirements
Nice to have
• I want the design to be clean and professional since it is focused on business executives

```html
<!DOCTYPE html>
<html lang="en">
<head>
<meta charset="utf-8">
<title>Golden Years Wellness Roadmap — Book Cover</title>
<link href="https://fonts.googleapis.com/css2?family=Josefin+Sans:wght@300;400&family=Montserrat:wght@400;600&display=swap" rel="stylesheet">
<style>
  :root {
    --backdrop: #eeebe6;
    --navy: #0c2340;
    --navy-deep: #081a31;
    --ink-white: #f4f6f9;
    --sub-white: #c9d3df;
    --band-white: #f7f8fa;
    --author-ink: #1d2a3a;
    --blueprint-light: #a9d3ea;
    --blueprint-mid: #5f93b8;
    --blueprint-dark: #1e3b5c;
  }
  * { margin: 0; padding: 0; box-sizing: border-box; }
  html, body {
    width: 1200px;
    height: 1200px;
    overflow: hidden;
    background: var(--backdrop);
  }
  .canvas {
    position: relative;
    width: 1200px;
    height: 1200px;
    display: flex;
    align-items: center;
    justify-content: center;
  }
  .book-cover {
    position: relative;
    width: 720px;
    height: 1120px;
    background: var(--navy);
    overflow: hidden;
    box-shadow: 0 10px 30px rgba(0, 0, 0, 0.18);
  }
  .cover-title {
    position: absolute;
    top: 98px;
    left: 0;
    right: 0;
    text-align: center;
    font-family: "Josefin Sans", sans-serif;
    font-weight: 400;
    color: var(--ink-white);
    font-size: 76px;
    line-height: 118px;
    letter-spacing: 6px;
    text-transform: uppercase;
  }
  .cover-subtitle {
    position: absolute;
    top: 486px;
    left: 90px;
    right: 90px;
    text-align: center;
    font-family: "Montserrat", sans-serif;
    font-weight: 400;
    color: var(--sub-white);
    font-size: 19px;
    line-height: 28px;
  }
  .cover-scene {
    position: absolute;
    left: 0;
    right: 0;
    top: 570px;
    bottom: 0;
    background:
      radial-gradient(ellipse 55% 45% at 45% 40%, rgba(70, 110, 150, 0.45), transparent 70%),
      linear-gradient(180deg, var(--navy) 0%, #12304f 35%, var(--blueprint-dark) 62%, var(--blueprint-mid) 82%, var(--blueprint-light) 100%);
  }
  .author-band {
    position: absolute;
    left: 0;
    right: 0;
    top: 955px;
    height: 58px;
    background: var(--band-white);
    display: flex;
    align-items: center;
    justify-content: center;
    gap: 18px;
    font-family: "Montserrat", sans-serif;
    font-weight: 600;
    font-size: 21px;
    color: var(--author-ink);
  }
  .author-sep {
    width: 6px;
    height: 6px;
    border-radius: 50%;
    background: var(--author-ink);
  }
</style>
</head>
<body>
  <main class="canvas">
    <section class="book-cover">
      <h1 class="cover-title">Golden Years<br>Wellness<br>Roadmap</h1>
      <p class="cover-subtitle">A No-Expense Method for Finishing Your<br>Later-Life Mosaic with Pooled KVB Care Schemes</p>
      <div class="cover-scene" role="img" aria-label="Photograph of a professional's hand drawing with a pen over architectural blueprints on a desk, in deep navy and light blue tones"></div>
      <div class="author-band">
        <span class="author-name">Derek Holloway</span>
        <span class="author-sep"></span>
        <span class="author-name">Neil Osgrove</span>
        <span class="author-sep"></span>
        <span class="author-name">Martin Quarles</span>
      </div>
    </section>
  </main>
</body>
</html>
```